Bold Plum

I am starting a sharpening service for knives, scissors, and garden tools. It's a sole proprietorship, so it's a small business. The business name is "Bolt Plum." A one or two-page website is fine. Ember Guild has created a logo for me. There should be pictures of the things I sharpen. There will also be a price list for sharpened items. My address is: 18392 Calloway Lane, Stevenson Ranch, CA 91307. Phone number is 661-555-0172

```html
<!DOCTYPE html>
<html lang="en">
<head>
<meta charset="utf-8">
<title>Bold Plum — Precision Sharpening</title>
<link href="https://fonts.googleapis.com/css2?family=Bebas+Neue&family=Plus+Jakarta+Sans:wght@400;500;600;700;800&display=swap" rel="stylesheet">
<style>
:root{
  --orange:#f5861f;
  --ink:#1b1b1b;
  --charcoal:#2b2b2b;
  --text:#333;
  --light:#f6f6f6;
  --white:#fff;
}
*{box-sizing:border-box;margin:0;padding:0}
html,body{width:1200px;height:4598px;overflow:hidden}
body{font-family:"Plus Jakarta Sans",Arial,sans-serif;color:var(--text);background:var(--white);position:relative}
.display{font-family:"Bebas Neue",Impact,sans-serif;font-weight:400;letter-spacing:.5px;line-height:1}
.abs{position:absolute}
.photo{position:absolute}
.underline{width:70px;height:3px;background:var(--orange);border-radius:2px}
.btn{position:absolute;display:flex;align-items:center;justify-content:center;gap:8px;border-radius:30px;font-size:13px;font-weight:800;text-transform:uppercase;letter-spacing:.3px;text-decoration:none}
.btn-orange{background:var(--orange);color:var(--white)}
.btn-outline{border:1.5px solid var(--white);color:var(--white)}
.btn-dark{background:var(--ink);color:var(--white)}

/* brand placeholder */
.brand{position:absolute;display:flex;align-items:center;gap:10px;font-family:"Plus Jakarta Sans",Arial,sans-serif;font-weight:800;white-space:nowrap}
.brand .mark{width:22px;height:22px;border-radius:50%;background:var(--orange);flex:none}

/* header */
.site-header{position:absolute;top:0;left:0;width:1200px;height:68px;background:var(--white);z-index:5}
.site-header .brand{left:146px;top:20px;font-size:24px;color:var(--ink)}
.main-nav a{position:absolute;top:26px;white-space:nowrap;font-size:13px;font-weight:700;color:var(--ink);text-decoration:none}
.main-nav a.active{color:var(--orange)}
.main-nav a.active::after{content:"";position:absolute;left:0;right:0;bottom:-8px;height:2px;background:var(--orange)}
.phone-pill{position:absolute;left:893px;top:14px;width:195px;height:40px;border-radius:20px;background:var(--orange);color:var(--white);font-size:15px;font-weight:700;display:flex;align-items:center;gap:14px;padding-left:6px}
.phone-pill .dot{width:30px;height:30px;border-radius:50%;background:var(--white);display:flex;align-items:center;justify-content:center}

/* hero */
.hero{position:absolute;top:68px;left:0;width:1200px;height:659px;background:linear-gradient(100deg,#121212 0%,#1d1d1d 38%,#4a4540 62%,#7a6a5c 80%,#3a3430 100%)}
.hero-kicker{position:absolute;left:120px;top:160px;color:var(--orange);font-size:20px;letter-spacing:2px;font-weight:500}
.hero-title{position:absolute;left:120px;top:192px;color:var(--white);font-size:64px}
.hero-list{position:absolute;left:120px;top:326px;list-style:none;color:var(--white);font-size:17px;font-weight:700}
.hero-list li{display:flex;align-items:center;gap:8px;height:33px}
.hero-arrow{position:absolute;top:270px}

/* about */
.about{position:absolute;top:727px;left:0;width:1200px;height:623px;background:var(--white);overflow:hidden}
.about-wedge{position:absolute;left:0;top:0}
.about-frame{position:absolute;left:93px;top:74px;width:150px;height:200px;background:#fbe1c6;border:2px solid var(--white)}
.about h2{position:absolute;left:645px;top:125px;font-size:58px;color:var(--ink)}
.about .underline{position:absolute;left:645px;top:193px}
.about p{position:absolute;left:648px;width:485px;font-size:16px;line-height:27px;color:var(--text)}

/* services */
.services{position:absolute;top:1350px;left:0;width:1200px;height:557px}
.services-band{position:absolute;top:0;left:0;width:1200px;height:454px;background:linear-gradient(90deg,#232323,#3b3b3b 50%,#262626)}
.services h2{position:absolute;top:110px;left:0;width:1200px;text-align:center;color:var(--white);font-size:56px}
.services .underline{position:absolute;left:565px;top:168px}
.service-card{position:absolute;top:215px;width:328px;height:341px;background:var(--white);box-shadow:0 2px 6px rgba(0,0,0,.18)}
.service-card .photo{left:0;top:0;width:328px;height:240px}
.service-card h3{position:absolute;top:262px;width:100%;text-align:center;font-size:19px;font-weight:600;color:var(--ink);letter-spacing:.5px}
.service-card p{position:absolute;top:295px;width:100%;text-align:center;font-size:13px;color:#555}

/* how it works */
.how{position:absolute;top:1947px;left:0;width:1200px;height:616px;background:linear-gradient(90deg,#f3f3f3,#fff 30%,#fff 70%,#f2f2f2)}
.how h2{position:absolute;top:45px;width:100%;text-align:center;font-size:54px;color:var(--ink)}
.how .lead{position:absolute;top:132px;width:100%;text-align:center;font-size:17px;color:var(--ink)}
.step{position:absolute;width:290px;height:290px;top:200px}
.step-title{position:absolute;top:162px;width:100%;text-align:center;font-size:17px;font-weight:700;color:var(--ink)}
.step-text{position:absolute;top:188px;left:50px;width:190px;text-align:center;font-size:14px;line-height:19px;color:#555}
.step-num{position:absolute;left:126px;top:270px;width:38px;height:38px;border-radius:50%;background:var(--orange);color:var(--white);font-family:"Bebas Neue",Impact,sans-serif;font-size:20px;display:flex;align-items:center;justify-content:center}

/* pricing */
.pricing{position:absolute;top:2563px;left:0;width:1200px;height:598px}
.pricing-copy{position:absolute;left:0;top:0;width:627px;height:598px;background:var(--light)}
.pricing h2{position:absolute;left:138px;top:82px;font-size:58px;color:var(--ink)}
.pricing .underline{position:absolute;left:138px;top:146px}
.pricing .lead{position:absolute;left:140px;top:172px;width:420px;font-size:17px;line-height:23px;color:#555}
.price-list{position:absolute;left:138px;top:250px;width:399px;list-style:none}
.price-list li{height:57px;border-bottom:1.5px solid #bbb;display:flex;align-items:center;font-size:19px;color:var(--ink);font-weight:500}
.price-list li:last-child{border-bottom:none}
.price-list .ico{width:56px}
.price-list .amt{margin-left:auto;width:80px;font-weight:800}

/* reviews */
.reviews{position:absolute;top:3161px;left:0;width:1200px;height:518px;background:var(--white)}
.reviews h2{position:absolute;top:78px;width:100%;text-align:center;font-size:56px;color:var(--ink)}
.reviews .underline{position:absolute;left:565px;top:140px}
.review-card{position:absolute;top:176px;width:302px;height:238px;border:1.5px solid #e1e1e1;background:var(--white);padding:34px 38px}
.stars{color:var(--orange);font-size:20px;letter-spacing:1px;line-height:1}
.review-card p{margin-top:12px;font-size:13px;line-height:21.5px;color:var(--ink)}
.review-card .who{margin-top:12px;font-size:14px;font-weight:800;color:var(--ink)}
.slide-btn{position:absolute;top:3322px;width:42px;height:42px;border-radius:50%;background:var(--white);box-shadow:0 2px 8px rgba(0,0,0,.15);display:flex;align-items:center;justify-content:center}

/* contact */
.contact{position:absolute;top:3679px;left:0;width:1200px;height:598px;background:linear-gradient(115deg,#f09a3e 0%,var(--orange) 40%,#f08a24 100%)}
.contact .kicker{position:absolute;left:162px;top:126px;font-size:13px;color:var(--white);letter-spacing:2px;font-weight:600}
.contact h2{position:absolute;left:162px;top:146px;font-size:54px;color:var(--white)}
.contact .underline{position:absolute;left:162px;top:202px;background:var(--white)}
.info{position:absolute;left:162px;display:flex;gap:18px;color:var(--white)}
.info .pin{width:34px;height:34px;border-radius:50%;background:var(--white);display:flex;align-items:center;justify-content:center;flex:none;margin-top:4px}
.info .label{font-size:16px;font-weight:500;opacity:.9}
.info .val{font-size:16px;font-weight:800;line-height:21px}
.contact-form{position:absolute;left:567px;top:98px;width:521px;height:456px;background:var(--charcoal);border-radius:4px}
.field{position:absolute;background:var(--white);border-radius:2px;height:46px;display:flex;align-items:center;gap:10px;padding-left:20px;font-size:13px;color:#333;font-weight:500}
.field svg{flex:none}
.field.area{align-items:flex-start;padding-top:16px;height:88px}

/* footer */
.site-footer{position:absolute;top:4277px;left:0;width:1200px;height:321px;background:#0b0b0b;color:var(--white)}
.site-footer .brand{left:170px;top:62px;font-size:26px;color:var(--white)}
.foot-nav{position:absolute;left:387px;top:67px;display:flex;align-items:center;font-size:14px;font-weight:700}
.foot-nav .sep{width:5px;height:5px;border-radius:50%;background:var(--orange);margin:0 30px}
.foot-rule{position:absolute;left:162px;width:876px;height:1px;background:#333}
.foot-info{position:absolute;top:168px;display:flex;align-items:center;gap:14px;font-size:13px}
.foot-info .pin{width:28px;height:28px;border-radius:50%;background:var(--white);display:flex;align-items:center;justify-content:center}
.foot-info b{display:block;font-weight:800}
.socials{position:absolute;left:882px;top:176px;display:flex;gap:6px}
.socials span{width:28px;height:28px;border-radius:50%;background:var(--white)}
.socials span:first-child{background:var(--orange)}
.copyright{position:absolute;top:290px;width:100%;text-align:center;font-size:11px;color:#aaa}
</style>
</head>
<body>

<header class="site-header">
  <div class="brand"><span class="mark"></span>BOLD PLUM</div>
  <nav class="main-nav">
    <a class="active" style="left:372px">HOME</a>
    <a style="left:458px">ABOUT US</a>
    <a style="left:575px">SERVICES</a>
    <a style="left:686px">PRICING</a>
    <a style="left:790px">CONTACT</a>
  </nav>
  <div class="phone-pill"><span class="dot"><svg width="16" height="16" viewBox="0 0 24 24"><path fill="#f5861f" d="M6.6 10.8a15.1 15.1 0 0 0 6.6 6.6l2.2-2.2c.3-.3.7-.4 1-.2 1.1.4 2.3.6 3.6.6.6 0 1 .4 1 1V20c0 .6-.4 1-1 1A17 17 0 0 1 3 4c0-.6.4-1 1-1h3.5c.6 0 1 .4 1 1 0 1.3.2 2.5.6 3.6.1.3 0 .7-.2 1z"/></svg></span>661-555-0172</div>
</header>

<section class="hero">
  <div class="photo" role="img" aria-label="Hands sharpening a blade against a spinning grinding wheel with sparks" style="left:560px;top:0;width:640px;height:659px;background:radial-gradient(ellipse at 45% 45%,#8a7c70 0%,#5a524b 40%,transparent 75%)"></div>
  <div class="hero-kicker">WELCOME TO BOLD PLUM</div>
  <h1 class="hero-title display">PRECISION SHARPENING<br>PROFESSIONAL RESULTS</h1>
  <ul class="hero-list">
    <li><svg width="16" height="14" viewBox="0 0 16 14"><path d="M1 7l5 5L15 1" stroke="#f5861f" stroke-width="2.4" fill="none"/></svg>Precision Sharpening</li>
    <li><svg width="16" height="14" viewBox="0 0 16 14"><path d="M1 7l5 5L15 1" stroke="#f5861f" stroke-width="2.4" fill="none"/></svg>Affordable pricing</li>
    <li><svg width="16" height="14" viewBox="0 0 16 14"><path d="M1 7l5 5L15 1" stroke="#f5861f" stroke-width="2.4" fill="none"/></svg>Local &amp; reliable service</li>
  </ul>
  <a class="btn btn-outline" style="left:120px;top:444px;width:181px;height:50px">View prices <svg width="14" height="12" viewBox="0 0 14 12"><path d="M0 6h12M7 1l5 5-5 5" stroke="#fff" stroke-width="2" fill="none"/></svg></a>
  <a class="btn btn-orange" style="left:309px;top:444px;width:180px;height:50px">Call us now <svg width="14" height="12" viewBox="0 0 14 12"><path d="M0 6h12M7 1l5 5-5 5" stroke="#fff" stroke-width="2" fill="none"/></svg></a>
  <svg class="hero-arrow" style="left:34px" width="20" height="32" viewBox="0 0 20 32"><path d="M17 2L3 16l14 14" stroke="#fff" stroke-width="3.5" fill="none"/></svg>
  <svg class="hero-arrow" style="left:1146px" width="20" height="32" viewBox="0 0 20 32"><path d="M3 2l14 14L3 30" stroke="#fff" stroke-width="3.5" fill="none"/></svg>
</section>

<section class="about">
  <svg class="about-wedge" width="400" height="623" viewBox="0 0 400 623"><polygon points="0,0 397,0 205,623 0,623" fill="#f5861f"/></svg>
  <div class="about-frame"></div>
  <div class="photo" role="img" aria-label="Teal bench grinder sharpening a blade with sparks" style="left:110px;top:86px;width:408px;height:207px;background:linear-gradient(135deg,#9aa3a3,#2b8d8e 45%,#5b6766)"></div>
  <div class="photo" role="img" aria-label="Hand holding a blade against a round sharpening stone" style="left:312px;top:303px;width:268px;height:238px;background:linear-gradient(135deg,#d6d6d6,#8a8a8a 55%,#3a3a3a)"></div>
  <div class="photo" role="img" aria-label="Set of kitchen knives" style="left:170px;top:410px;width:170px;height:95px;background:linear-gradient(160deg,#c8c8c8,#2a2a2a)"></div>
  <h2 class="display">ABOUT BOLD PLUM</h2>
  <div class="underline"></div>
  <p style="top:222px">Lorem ipsum dolor sit amet, consectetur adipiscing elit, sed do eiusmod tempor incididunt ut labore et dolore magna aliqua. Quis ipsum suspendisse ultrices gravida. Risus commodo viverra maecenas accumsan lacus vel facilisis.</p>
  <p style="top:360px">Lorem ipsum dolor sit amet, consectetur adipiscing elit, sed do eiusmod tempor incididunt ut labore et dolore</p>
  <a class="btn btn-orange" style="left:645px;top:444px;width:182px;height:48px">Call us now <svg width="14" height="12" viewBox="0 0 14 12"><path d="M0 6h12M7 1l5 5-5 5" stroke="#fff" stroke-width="2" fill="none"/></svg></a>
</section>

<section class="services">
  <div class="services-band" role="img" aria-label="Dark workshop backdrop with sharpening tools"></div>
  <h2 class="display">WHAT WE SHARPEN</h2>
  <div class="underline"></div>
  <article class="service-card" style="left:93px">
    <div class="photo" role="img" aria-label="Four kitchen knives on a wooden board" style="background:linear-gradient(90deg,#8c5a34,#b57a48 50%,#7a4a2a)"></div>
    <h3>KNIVES</h3><p>Kitchen, chef, hunting, pocket knives</p>
  </article>
  <article class="service-card" style="left:435px">
    <div class="photo" role="img" aria-label="Scissors being sharpened on a grinding wheel" style="background:linear-gradient(120deg,#6e6660,#b3a79d 50%,#4a423d)"></div>
    <h3>SCISSORS SHARPENING</h3><p>Household, salon, fabric, utility</p>
  </article>
  <article class="service-card" style="left:776px">
    <div class="photo" role="img" aria-label="Garden shears being sharpened" style="background:linear-gradient(120deg,#d0d0d0,#6e6e6e 55%,#2e2e2e)"></div>
    <h3>GARDEN TOOLS</h3><p>Shears, pruners, loppers, hedge tools</p>
  </article>
</section>

<section class="how">
  <h2 class="display">HOW IT WORKS</h2>
  <p class="lead">Lorem ipsum dolor sit amet, consectetur adipiscing elit, sed do eiusmod tempor inc</p>

  <div class="step" style="left:163px">
    <svg class="abs" width="290" height="290" viewBox="0 0 290 290"><circle cx="145" cy="145" r="138" fill="#fff" stroke="#e6e6e6" stroke-width="1.5"/><path d="M40 235A138 138 0 0 1 250 35" stroke="#cfcfcf" stroke-width="9" fill="none"/></svg>
    <svg class="abs" style="left:120px;top:80px" width="50" height="50" viewBox="0 0 24 24"><path fill="none" stroke="#f5861f" stroke-width="1.2" d="M6.6 10.8a15.1 15.1 0 0 0 6.6 6.6l2.2-2.2c.3-.3.7-.4 1-.2 1.1.4 2.3.6 3.6.6.6 0 1 .4 1 1V20c0 .6-.4 1-1 1A17 17 0 0 1 3 4c0-.6.4-1 1-1h3.5c.6 0 1 .4 1 1 0 1.3.2 2.5.6 3.6.1.3 0 .7-.2 1zM14 3a7 7 0 0 1 7 7M14 6a4 4 0 0 1 4 4"/></svg>
    <div class="step-title">Drop off or contact us</div>
    <div class="step-text">Lorem ipsum dolor sit amet consectetur</div>
    <div class="step-num">01</div>
  </div>
  <svg class="abs" style="left:418px;top:270px" width="80" height="40" viewBox="0 0 80 40"><path d="M2 28Q40 40 74 22M66 16l8 6-9 4" stroke="#999" stroke-width="1.5" fill="none"/></svg>

  <div class="step" style="left:475px;top:208px">
    <svg class="abs" width="290" height="290" viewBox="0 0 290 290"><circle cx="145" cy="145" r="138" fill="#fff" stroke="#e6e6e6" stroke-width="1.5"/><path d="M20 90A138 138 0 0 1 200 18" stroke="#cfcfcf" stroke-width="9" fill="none"/></svg>
    <svg class="abs" style="left:115px;top:60px" width="60" height="60" viewBox="0 0 60 60"><circle cx="34" cy="34" r="20" fill="none" stroke="#f5861f" stroke-width="1.5"/><circle cx="34" cy="34" r="11" fill="none" stroke="#f5861f" stroke-width="1.5"/><circle cx="34" cy="34" r="3" fill="#f5861f"/><path d="M4 46L28 22l4 4L8 50z" fill="none" stroke="#f5861f" stroke-width="1.5"/></svg>
    <div class="step-title">We sharpen your tools</div>
    <div class="step-text">Lorem ipsum dolor sit amet consectetur</div>
    <div class="step-num">02</div>
  </div>
  <svg class="abs" style="left:738px;top:267px" width="80" height="40" viewBox="0 0 80 40"><path d="M2 28Q40 8 74 22M66 14l8 8-10 3" stroke="#999" stroke-width="1.5" fill="none"/></svg>

  <div class="step" style="left:795px">
    <svg class="abs" width="290" height="290" viewBox="0 0 290 290"><circle cx="145" cy="145" r="138" fill="#fff" stroke="#e6e6e6" stroke-width="1.5"/><path d="M240 45A138 138 0 0 1 80 268" stroke="#cfcfcf" stroke-width="9" fill="none"/></svg>
    <svg class="abs" style="left:115px;top:62px" width="60" height="60" viewBox="0 0 60 60"><path d="M8 52l10-10 4 4-10 10zM20 40L50 8c3 4 2 10-2 14L24 44z" fill="none" stroke="#f5861f" stroke-width="1.6"/></svg>
    <div class="step-title">Pick up sharp results</div>
    <div class="step-text">Lorem ipsum dolor sit amet consectetur</div>
    <div class="step-num">03</div>
  </div>
</section>

<section class="pricing">
  <div class="pricing-copy">
    <h2 class="display">OUR PRICING</h2>
    <div class="underline"></div>
    <p class="lead">Lorem ipsum dolor sit amet, consectetur adipiscing elit, sed do eiusmod tempor incididunt</p>
    <ul class="price-list">
      <li><span class="ico"><svg width="36" height="30" viewBox="0 0 36 30"><path d="M4 4l22 20M24 22l6 6" stroke="#1b1b1b" stroke-width="3" stroke-linecap="round"/></svg></span>Standard Knife<span class="amt">$15</span></li>
      <li><span class="ico"><svg width="36" height="36" viewBox="0 0 36 36"><path d="M4 32l6-6 3 3-6 6zM12 25L32 4c2 4 1 8-2 11L15 28z" fill="#1b1b1b"/></svg></span>Large Knife<span class="amt">$25</span></li>
      <li><span class="ico"><svg width="36" height="36" viewBox="0 0 36 36"><circle cx="8" cy="28" r="4" fill="none" stroke="#1b1b1b" stroke-width="2"/><circle cx="16" cy="30" r="4" fill="none" stroke="#1b1b1b" stroke-width="2"/><path d="M11 25L30 4M14 26L24 8" stroke="#1b1b1b" stroke-width="2"/></svg></span>Scissors<span class="amt">$10</span></li>
      <li><span class="ico"><svg width="36" height="36" viewBox="0 0 36 36"><path d="M4 34l12-14M8 26l14-4M16 20l14-16M18 16l12 4" stroke="#1b1b1b" stroke-width="2" fill="none"/></svg></span>Garden Tools<span class="amt">$30</span></li>
    </ul>
  </div>
  <div class="photo" role="img" aria-label="Knives and kitchen scissors laid on a dark wooden table" style="left:627px;top:0;width:573px;height:598px;background:linear-gradient(135deg,#4a2e1c,#7a4f30 40%,#5a3820 70%,#3a2414)"></div>
</section>

<section class="reviews">
  <h2 class="display">REVIEWS</h2>
  <div class="underline"></div>
  <article class="review-card" style="left:135px"><div class="stars">★★★★★</div><p>“Lorem ipsum dolor sit amet, consectetur adipiscing elit, sed do eiusmod tempor incididunt ut labore et dolore magna aliqua Ut enim ad minim veniam, quis nostrud”</p><div class="who">Mara Lindqvist</div></article>
  <article class="review-card" style="left:455px"><div class="stars">★★★★★</div><p>“Lorem ipsum dolor sit amet, consectetur adipiscing elit, sed do eiusmod tempor incididunt ut labore et dolore magna aliqua Ut enim ad minim veniam, quis nostrud”</p><div class="who">Mara Lindqvist</div></article>
  <article class="review-card" style="left:773px"><div class="stars">★★★★★</div><p>“Lorem ipsum dolor sit amet, consectetur adipiscing elit, sed do eiusmod tempor incididunt ut labore et dolore magna aliqua Ut enim ad minim veniam, quis nostrud”</p><div class="who">Mara Lindqvist</div></article>
</section>
<div class="slide-btn" style="left:66px"><svg width="16" height="12" viewBox="0 0 16 12"><path d="M16 6H2M7 1L2 6l5 5" stroke="#3a7bd5" stroke-width="1.6" fill="none"/></svg></div>
<div class="slide-btn" style="left:1114px"><svg width="16" height="12" viewBox="0 0 16 12"><path d="M0 6h14M9 1l5 5-5 5" stroke="#3a7bd5" stroke-width="1.6" fill="none"/></svg></div>

<section class="contact">
  <div class="kicker">GET IN TOUCH</div>
  <h2 class="display">CONTACT US</h2>
  <div class="underline"></div>
  <div class="info" style="top:238px"><span class="pin"><svg width="14" height="18" viewBox="0 0 14 18"><path d="M7 0a7 7 0 0 1 7 7c0 5-7 11-7 11S0 12 0 7a7 7 0 0 1 7-7z" fill="#f5861f"/><circle cx="7" cy="7" r="2.5" fill="#fff"/></svg></span><div><div class="label">Address</div><div class="val">18392 Calloway Lane,<br>Stevenson Ranch, CA 91307</div></div></div>
  <div class="info" style="top:325px"><span class="pin"><svg width="16" height="16" viewBox="0 0 24 24"><path fill="#f5861f" d="M6.6 10.8a15.1 15.1 0 0 0 6.6 6.6l2.2-2.2c.3-.3.7-.4 1-.2 1.1.4 2.3.6 3.6.6.6 0 1 .4 1 1V20c0 .6-.4 1-1 1A17 17 0 0 1 3 4c0-.6.4-1 1-1h3.5c.6 0 1 .4 1 1 0 1.3.2 2.5.6 3.6.1.3 0 .7-.2 1z"/></svg></span><div><div class="label">Phone Number</div><div class="val">661-555-0172</div></div></div>
  <a class="btn btn-dark" style="left:157px;top:410px;width:196px;height:47px;font-size:14px">Call us now <svg width="14" height="12" viewBox="0 0 14 12"><path d="M0 6h12M7 1l5 5-5 5" stroke="#fff" stroke-width="2" fill="none"/></svg></a>

  <form class="contact-form">
    <div class="field" style="left:48px;top:60px;width:210px"><svg width="12" height="12" viewBox="0 0 12 12"><circle cx="6" cy="3.5" r="3" fill="#999"/><path d="M0 12a6 5 0 0 1 12 0z" fill="#999"/></svg>First Name*</div>
    <div class="field" style="left:268px;top:60px;width:210px"><svg width="12" height="12" viewBox="0 0 12 12"><circle cx="6" cy="3.5" r="3" fill="#999"/><path d="M0 12a6 5 0 0 1 12 0z" fill="#999"/></svg>Last Name*</div>
    <div class="field" style="left:48px;top:116px;width:430px"><svg width="14" height="10" viewBox="0 0 14 10"><rect width="14" height="10" fill="#999"/><path d="M0 0l7 5 7-5" stroke="#fff" fill="none"/></svg>Email address*</div>
    <div class="field" style="left:48px;top:172px;width:430px"><svg width="12" height="12" viewBox="0 0 24 24"><path fill="#999" d="M6.6 10.8a15.1 15.1 0 0 0 6.6 6.6l2.2-2.2c.3-.3.7-.4 1-.2 1.1.4 2.3.6 3.6.6.6 0 1 .4 1 1V20c0 .6-.4 1-1 1A17 17 0 0 1 3 4c0-.6.4-1 1-1h3.5c.6 0 1 .4 1 1 0 1.3.2 2.5.6 3.6.1.3 0 .7-.2 1z"/></svg>Phone*</div>
    <div class="field area" style="left:48px;top:228px;width:430px"><svg width="14" height="12" viewBox="0 0 14 12"><path d="M7 0C3 0 0 2.3 0 5c0 1.5.9 2.8 2.3 3.7L1.5 12l3.6-2.2c.6.1 1.2.2 1.9.2 4 0 7-2.3 7-5S11 0 7 0z" fill="#999"/></svg>Leave Message</div>
    <div class="btn btn-orange" style="left:48px;top:358px;width:200px;height:46px;letter-spacing:1.5px">Send message ›</div>
  </form>
</section>

<footer class="site-footer">
  <div class="brand"><span class="mark"></span>BOLD PLUM</div>
  <nav class="foot-nav"><span>HOME</span><span class="sep"></span><span>ABOUT US</span><span class="sep"></span><span>SERVICES</span><span class="sep"></span><span>PRICING</span><span class="sep"></span><span>CONTACT</span></nav>
  <div class="foot-rule" style="top:150px"></div>
  <div class="foot-info" style="left:226px"><span class="pin"><svg width="14" height="14" viewBox="0 0 24 24"><path fill="#0b0b0b" d="M6.6 10.8a15.1 15.1 0 0 0 6.6 6.6l2.2-2.2c.3-.3.7-.4 1-.2 1.1.4 2.3.6 3.6.6.6 0 1 .4 1 1V20c0 .6-.4 1-1 1A17 17 0 0 1 3 4c0-.6.4-1 1-1h3.5c.6 0 1 .4 1 1 0 1.3.2 2.5.6 3.6.1.3 0 .7-.2 1z"/></svg></span><div>Phone Number<b>661-555-0172</b></div></div>
  <div class="foot-info" style="left:446px"><span class="pin"><svg width="12" height="16" viewBox="0 0 14 18"><path d="M7 0a7 7 0 0 1 7 7c0 5-7 11-7 11S0 12 0 7a7 7 0 0 1 7-7z" fill="#0b0b0b"/><circle cx="7" cy="7" r="2.5" fill="#fff"/></svg></span><div>Address<b>18392 Calloway Lane, Stevenson Ranch, CA 91307</b></div></div>
  <div class="socials"><span></span><span></span><span></span></div>
  <div class="foot-rule" style="top:238px"></div>
  <div class="copyright">© 2026 Bold Plum. All Rights Reserved</div>
</footer>

</body>
</html>
```